Web Design For Manufacturing And Outsourcing Company

Pick up the pieces from our previous developer and help us complete our website.

5 pages - Home,Machining,Sourcing,About Us, and Contact

Attached you will find screen shots of previous direction but we're open to new ideas.

We can provide all text and images needed.

Thanks!

5+ page

```html
<!DOCTYPE html>
<html lang="en">
<head>
<meta charset="UTF-8">
<title>Vale Industries</title>
<link href="https://fonts.googleapis.com/css2?family=Roboto+Condensed:wght@400;700&display=swap" rel="stylesheet">
<style>
:root{
  --orange:#ff7321;
  --ink:#151515;
  --white:#ffffff;
  --band:#292929;
  --footer:#101010;
  --muted:#9a9a9a;
}
*{margin:0;padding:0;box-sizing:border-box}
html,body{width:1200px;height:2571px;overflow:hidden}
body{position:relative;font-family:"Roboto Condensed",Arial,sans-serif;color:var(--white);background:var(--footer)}
.abs{position:absolute}

/* header & hero */
.hero{left:0;top:0;width:1200px;height:640px;background:radial-gradient(ellipse at 70% 40%,#4a5a66 0%,#26313a 45%,#0e1216 100%)}
.brand{left:172px;top:28px;display:flex;align-items:center;gap:10px;font-size:19px;font-weight:700;letter-spacing:2px;line-height:24px}
.brand-square{width:18px;height:18px;background:var(--white)}
.nav{display:flex;font-size:15px}
.nav-top{left:583px;top:31px;gap:22px}
.lang{left:970px;top:25px;width:48px;height:30px;border:1px solid #888;font-size:12px;display:flex;align-items:center;justify-content:center;gap:5px;color:#ddd}
.lang svg{width:8px;height:6px}
.headline{left:0;top:252px;width:1200px;text-align:center;font-size:64px;font-weight:700;line-height:82px;letter-spacing:-0.5px}
.headline .framed{display:inline-block;border:3px solid var(--orange);padding:0 12px;margin-left:4px}
.what{left:0;top:494px;width:1200px;text-align:center;font-size:24px;letter-spacing:8px}
.what-arrow{left:588px;top:540px}

/* service rows */
.photo-machining{left:0;top:640px;width:648px;height:640px;background:radial-gradient(circle at 50% 62%,#e39a4a 0%,#6d5544 22%,#2b2a2a 55%,#141414 100%)}
.panel-machining{left:648px;top:640px;width:552px;height:640px;background:var(--orange)}
.panel-sourcing{left:0;top:1280px;width:550px;height:640px;background:var(--orange)}
.photo-sourcing{left:550px;top:1280px;width:650px;height:640px;background:radial-gradient(circle at 48% 42%,#f0a55a 0%,#8a4b2a 16%,#2e3a48 45%,#182029 100%)}
.service-title{font-size:48px;font-weight:400;line-height:56px}
.service-copy{width:350px;font-size:15.5px;line-height:23.5px;margin-top:24px}
.btn{display:flex;align-items:center;justify-content:center;font-size:16px;font-weight:700;letter-spacing:4px}
.btn-dark{width:201px;height:67px;background:var(--ink);margin-top:54px}
.service-text{top:738px;left:716px}
.service-text.left{top:1378px;left:134px}

/* call to action */
.cta{left:0;top:1920px;width:1200px;height:380px;background:radial-gradient(circle at 36% 58%,#3b3b3b 0%,#232323 30%,#141414 62%,#111 100%)}
.cta-line{left:0;top:2022px;width:1200px;text-align:center;font-size:38px}
.cta-line strong{color:var(--orange);font-weight:700}
.btn-orange{left:492px;top:2114px;width:216px;height:67px;background:var(--orange);font-size:19px;letter-spacing:5px}

/* social band */
.band{left:0;top:2300px;width:1200px;height:129px;background:var(--band)}
.band-copy{left:247px;top:2351px;font-size:19px;color:var(--muted)}
.social{top:2344px;width:42px;height:42px;border-radius:50%;background:var(--orange)}

/* footer */
.footer-brand{left:296px;top:2480px;font-size:14px;font-weight:700;letter-spacing:1px;line-height:20px;color:var(--white)}
.nav-foot{top:2466px;left:440px;gap:0;font-size:14px}
.nav-foot span{display:inline-block}
.copyright{left:440px;top:2510px;font-size:13px;color:#8a8a8a}
</style>
</head>
<body>

<header>
  <div class="abs hero" role="img" aria-label="Close-up photograph of a machined steel part under a milling tool"></div>
  <div class="abs brand"><span class="brand-square"></span><span>VALE INDUSTRIES</span></div>
  <nav class="abs nav nav-top"><span>Home</span><span>Machining</span><span>Sourcing</span><span>About Us</span><span>Contact</span></nav>
  <div class="abs lang">EN <svg viewBox="0 0 8 6"><path d="M0 0h8L4 6z" fill="#ddd"/></svg></div>
  <h1 class="abs headline">Quality <span class="framed">Goods and Services</span></h1>
  <div class="abs what">WHAT WE DO</div>
  <svg class="abs what-arrow" width="24" height="18" viewBox="0 0 24 18"><path d="M0 0h24L12 18z" fill="var(--orange)"/></svg>
</header>

<main>
  <section>
    <div class="abs photo-machining" role="img" aria-label="Photograph of hands operating a metal lathe with glowing cutting point"></div>
    <div class="abs panel-machining"></div>
    <div class="abs service-text">
      <h2 class="service-title">Machining</h2>
      <p class="service-copy">Lorem ipsum dolor sit amet, consectetur adipisicing elit, sed do eiusmod tempor incididunt ut labore et dolore magna aliqua. Ut enim ad minim veniam, quis nostrud exercitation ullamco laboris nisi ut aliquip ex ea commodo consequat. Duis aute irure dolor in rep rehenderit in voluptate velit esse cillum dolore eu fugiat nulla pariatur. Excepteur sint occaecat cupi datat non proident, sunt in culpa</p>
      <div class="btn btn-dark">LEARN MORE</div>
    </div>
  </section>

  <section>
    <div class="abs panel-sourcing"></div>
    <div class="abs photo-sourcing" role="img" aria-label="Photograph of a hand holding a glowing globe surrounded by energy and resource icons"></div>
    <div class="abs service-text left">
      <h2 class="service-title">Sourcing</h2>
      <p class="service-copy">Lorem ipsum dolor sit amet, consectetur adipisicing elit, sed do eiusmod tempor incididunt ut labore et dolore magna aliqua. Ut enim ad minim veniam, quis nostrud exercitation ullamco laboris nisi ut aliquip ex ea commodo consequat. Duis aute irure dolor in rep rehenderit in voluptate velit esse cillum dolore eu fugiat nulla pariatur. Excepteur sint occaecat cupi datat non proident, sunt in culpa</p>
      <div class="btn btn-dark">LEARN MORE</div>
    </div>
  </section>

  <section>
    <div class="abs cta" role="img" aria-label="Top-down photograph of hands typing on a laptop on a round table"></div>
    <p class="abs cta-line">Looking for <strong>Machining</strong> or <strong>Sourcing</strong> services?</p>
    <div class="abs btn btn-orange">CONTACT US</div>
  </section>
</main>

<footer>
  <div class="abs band"></div>
  <p class="abs band-copy">Lorem ipsum dolor sit amet, consectetur adipisicing elit</p>
  <span class="abs social" style="left:777px" aria-label="Social link"></span>
  <span class="abs social" style="left:845px" aria-label="Social link"></span>
  <span class="abs social" style="left:910px" aria-label="Social link"></span>

  <div class="abs footer-brand">VALE INDUSTRIES</div>
  <nav class="abs nav nav-foot">
    <span style="width:76px">Home</span><span style="width:104px">Machining</span><span style="width:87px">Sourcing</span><span style="width:97px">About Us</span><span>Contact</span>
  </nav>
  <p class="abs copyright">Copyright 2018. Vale Industries. All rights reserved.</p>
</footer>

</body>
</html>
```